The Tidy Lantern Business Card

I need a business card designed for The Tidy Lantern. The company provides on site support and education to end consumers in the ins and outs of all our digital devices. We advise on product purchase, installation, maintenance and troubleshooting. Anything from cordless phones to home networks.
My initial concept is double sided with the white logo on green on one side and contact details and a small logo on the flip side (logo package attached)
Contact Details:
Miles Fenwright
Managing Director
PO Box 43
Brackton, NSW 2187
Phone: 0438 907 516
email: miles@tidylantern.com.au
web: www.tidylantern.com.au
Target Market(s)
Busy professionals and retired folks.
Industry/Entity Type
Education
Look and feel

```html
<!DOCTYPE html>
<html lang="en">
<head>
<meta charset="utf-8">
<title>The Tidy Lantern – Business Card</title>
<link rel="stylesheet" href="https://fonts.googleapis.com/css2?family=Roboto:wght@300;400&display=swap">
<style>
  :root {
    --backdrop: #e4e5e7;
    --green-light: #a6d63a;
    --green-mid: #7cc220;
    --green-deep: #3fa82a;
    --white: #ffffff;
    --ink: #2b2b2b;
    --ink-soft: #8a8a8a;
    --rule: #b7dc3c;
    --accent: #8cc63f;
  }
  * { margin: 0; padding: 0; box-sizing: border-box; }
  html, body {
    width: 1200px; height: 800px; overflow: hidden;
    background: var(--backdrop);
    font-family: "Roboto", Arial, sans-serif;
  }
  .canvas {
    position: relative; width: 1200px; height: 800px;
    display: flex; align-items: center; justify-content: center; gap: 60px;
  }
  .card {
    position: relative; width: 525px; height: 300px;
    border-radius: 4px; overflow: hidden;
    box-shadow: 0 10px 24px rgba(0,0,0,0.14);
  }

  /* Front side */
  .card-front {
    background: linear-gradient(135deg, var(--green-light) 0%, var(--green-mid) 60%, #6cb81c 100%);
  }
  .front-texture {
    position: absolute; inset: 0;
    background:
      radial-gradient(ellipse 60% 45% at 55% 50%, rgba(255,255,255,0.22), transparent 70%),
      radial-gradient(ellipse 80% 30% at 70% 75%, rgba(255,255,255,0.10), transparent 70%);
  }
  .front-brand {
    position: absolute; left: 0; right: 0; top: 50%;
    transform: translateY(-50%);
    display: flex; align-items: center; justify-content: center; gap: 14px;
  }
  .brand-dot {
    width: 22px; height: 22px; border-radius: 50%;
    background: var(--white);
  }
  .brand-name {
    color: var(--white); font-weight: 300; font-size: 38px; letter-spacing: 1px;
  }

  /* Back side */
  .card-back { background: var(--white); }
  .back-art {
    position: absolute; left: 0; top: 0; width: 240px; height: 300px;
  }
  .back-content {
    position: absolute; left: 238px; top: 74px; right: 30px;
  }
  .holder-name {
    font-size: 24px; font-weight: 300; color: var(--ink); line-height: 1.1;
  }
  .holder-title {
    font-size: 13px; font-weight: 300; color: var(--ink-soft); margin-top: 3px;
  }
  .divider {
    height: 1px; background: var(--rule); margin: 12px 0 12px; width: 250px;
  }
  .contact-list { list-style: none; font-size: 14px; font-weight: 300; color: var(--ink); line-height: 19px; }
  .contact-list li { display: flex; align-items: center; gap: 8px; }
  .contact-list .indent { padding-left: 20px; }
  .contact-icon { width: 12px; height: 12px; flex: none; }
  .contact-web { color: var(--accent); }
  .contact-web .domain { color: var(--ink); }
  .contact-web .domain-tail { color: var(--accent); }
</style>
</head>
<body>
<main class="canvas">

  <section class="card card-front" aria-label="Business card front">
    <div class="front-texture" role="img" aria-label="Soft light green leaf-shaped glow pattern"></div>
    <div class="front-brand">
      <span class="brand-dot"></span>
      <span class="brand-name">The Tidy Lantern</span>
    </div>
  </section>

  <section class="card card-back" aria-label="Business card back">
    <svg class="back-art" viewBox="0 0 240 300" role="img" aria-label="Faceted green panel with a faint large brand decoration">
      <defs>
        <linearGradient id="facet" x1="0" y1="0" x2="1" y2="1">
          <stop offset="0" stop-color="#b3dc45"/>
          <stop offset="0.55" stop-color="#55b42c"/>
          <stop offset="1" stop-color="#2f9a2a"/>
        </linearGradient>
      </defs>
      <polygon points="0,0 215,0 230,95 150,205 85,270 0,300" fill="url(#facet)"/>
      <polygon points="0,0 215,0 120,120 0,90" fill="rgba(255,255,255,0.18)"/>
      <polygon points="120,120 230,95 150,205" fill="rgba(0,0,0,0.06)"/>
    </svg>

    <div class="back-content">
      <h1 class="holder-name">Miles Fenwright</h1>
      <p class="holder-title">Managing Director</p>
      <div class="divider"></div>
      <ul class="contact-list">
        <li>
          <svg class="contact-icon" viewBox="0 0 12 12" aria-hidden="true"><path d="M6 0.5a3.6 3.6 0 0 0-3.6 3.6C2.4 7 6 11.5 6 11.5S9.6 7 9.6 4.1A3.6 3.6 0 0 0 6 0.5zm0 5a1.4 1.4 0 1 1 0-2.8 1.4 1.4 0 0 1 0 2.8z" fill="#8cc63f"/></svg>
          PO Box 43
        </li>
        <li class="indent">Brackton, NSW 2187</li>
        <li>
          <svg class="contact-icon" viewBox="0 0 12 12" aria-hidden="true"><circle cx="6" cy="6" r="5.3" fill="none" stroke="#8cc63f" stroke-width="1"/><path d="M4.2 3.2l1 1-.6.8c.4.8 1 1.4 1.8 1.8l.8-.6 1 1-.7.9C5.6 8 4 6.4 3.3 3.9z" fill="#8cc63f"/></svg>
          0438 907 516
        </li>
        <li>
          <svg class="contact-icon" viewBox="0 0 12 12" aria-hidden="true"><rect x="0.8" y="2.5" width="10.4" height="7" fill="none" stroke="#8cc63f" stroke-width="1"/><path d="M0.8 2.5L6 6.6l5.2-4.1" fill="none" stroke="#8cc63f" stroke-width="1"/></svg>
          miles@tidylantern.com.au
        </li>
        <li class="contact-web">www.<span class="domain">tidylantern</span><span class="domain-tail">.com.au</span></li>
      </ul>
    </div>
  </section>

</main>
</body>
</html>
```